Greek Souvlaki Restaurant Menu Design

We would like to redesign our menu (at the moment just a price-list without any graphics) and create something more fun.

You can find all the items we are offering at the following link / our e-shop:
https://fennelandfig.example/orders/en/order/
I have also attached a printout of the above with hand written notes on the sections and items that will be included.

Our menu is divided to a couple of parts:
- Souvlaki Bar and Grill
- Authentic Greek Cuisine
- Wine List
- Desserts
- Bakaliko

This project will take on the first part of our menu, which is the Souvlaki Bar and Grill. If we are happy with your design, we will then develop the rest of our menu.

Souvlaki Bar and Grill
---------------------------

Our souvlaki can be customised to the customer requirements. The following links have similar set ups:

WOWZA!Bun
https://pinboard.example/pin/100000000000000001/
I like the way they have set it up, but the graphics and colours used are not my thing. I also like they way they have split up the steps, choose, top it of, etc.

The Crisp
https://pinboard.example/pin/100000000000000002/
I hate the step 1,2,3 on the left side. It does not make it playful. Like the fact that they have used pictures of the ingredients.

https://pinboard.example/pin/100000000000000003/
Hate the graphics, like the concept.

-------------

First Sections: Our Souvliaki Pita Wrap

The steps to customise a souvlaki can be found on the following link:
https://fennelandfig.example/orders/en/order/ and choose pita wrap.

Most of the one side of our Souvliaki/Grill menu should be dedicated to our Pita Wraps.

It should have a small description of the Greek Souvlaki Pita Wrap. Something along the lines of "Get a whole meal all wrapped up with our delicious Greek Pita Wraps. Containing protein, sauce and salad". Improvements of this line are welcome.

It should then have the steps to customise it.

Step One.
Choose Base:
1. Chicken Skewer
2. Pork Skewer
3. etc
Price and options can be found on the above link on our website

Step Two.
Add one of our delicious home made sauces.
Options can be found on our website.

Step Three
Finalise it with the ingredients of your choice.
The customer can select multiple incredients

Step Four.
Feeling Hungry? Add extras:
Extras and Prices can be found on the link provided.

Buy two wraps and save. Takeaway only!
You will find this option as "Double Souvlaki Pita Wrap Offer."
Instead of 2x5.5 = £11 pay £10.5. This offer should also be mentioned somewhere on this section.

-----

Second Section - Our Platters

Skewers Platter and Gyros Platter

Options can be found by clicking on the items on the link provided.

Extras and Pita Bread option are common. Meat options are different and skewers have a choice of side. Meat options have 2/3 skewers and 200/300 grams of gyros, so they can probably be combined somehow.

These section can also be called Naked / Open Souvlaki Platters

Third Section
From Our Grill

All options from this section together with modifiers (can be see if you click on each item). I would like pictures from each item.

Forth Section
Meal Deals, starter combo and Set Menu.

Meal Deal for 1/2 and 4 are wraps with extras. The for 4 is not on the pdf and will be up on our website soon, so please check. I think those are easy to e incorporated next to the pita wrap section as upgrades to save.

Set menus are various items.

If they can fit on this page somehow we incorporate them, if not we can make a separate page with the offers / meals deals. If a separate page is created them the meal deal from our kitchen and vegetarean set menu should also be included.

Fifth Section
Salads and Starter

I would like all options from Hot and Cold starter and our salad. I would like pictures next to all options, if possible.

-----

Final notes/ideas.

Wraps, platters and grill could be one page front and back. Salads and starters could be a different page(s) or sections.

The menu should be easily updated and we would like a format where we can update prices and descriptions.

Prices and descriptions can be found on the link provided.

Feel free to improve our descriptions and titles. Please do mention where you made improvements, so we can approve them.

Our kitchen, dessert and wine menu will be given as a separate project and priority will be given to the person that won this competition.

If you need better quality pictures please let us know, most of the pictures we do have them in raw format too.

------

Some designs that I like. To give you an idea of the design I would like to see:

https://www.craftstall.example/listing/200000001/american-menu-restaurant-cafe-menus
I would love to see something like that for the grill/salad/starter side of our menu, since it has space for pictures.

https://pinboard.example/pin/100000000000000004/
I would love to see something like that, where the incredients of a souvlaki come together. This is optional and does not have to be there.

https://pinboard.example/pin/100000000000000005/

https://pinboard.example/pin/100000000000000006/

https://pinboard.example/pin/100000000000000007/

https://pinboard.example/pin/100000000000000008/

Target Market(s)

London

Font styles to use
Serif
Sans Serif

Colors
abd037
3277b5
33a6d7

Requirements
Must have
• Build your own souvlaki section. See description for examples.

Pictures for starters and salads.

Should be elegant
Nice to have
• Incorporate our relevant meal deals on the souvlaki pita section

```html
<!DOCTYPE html>
<html lang="en">
<head>
<meta charset="utf-8">
<title>Fennel &amp; Fig – Souvlaki Bar and Grill Menu</title>
<link rel="stylesheet" href="https://fonts.googleapis.com/css2?family=Yanone+Kaffeesatz:wght@400;600&family=Montserrat:wght@400;600&family=Fira+Sans:wght@800&family=Lora:ital@1&display=swap">
<style>
:root{
  --backdrop:#84a22e;
  --board:#1d1d1d;
  --board-edge:#111;
  --band:#7ea22f;
  --accent:#9cc63d;
  --text:#c9c9c9;
  --text-dim:#9a9a9a;
  --white:#f2f2f2;
  --pin:#d2202a;
  --rule:#6f8f2a;
}
*{margin:0;padding:0;box-sizing:border-box}
html,body{width:1200px;height:2399px;overflow:hidden;background:var(--backdrop)}
.stage{position:relative;width:1288px;height:2576px;transform:scale(0.93168);transform-origin:0 0}
.page{position:absolute;width:501px;height:709px;background:radial-gradient(circle at 30% 20%,#262626 0,var(--board) 55%,#181818 100%);box-shadow:6px 8px 14px rgba(0,0,0,.45);overflow:hidden;font-family:"Montserrat",sans-serif;color:var(--text)}
.p1{left:393px;top:117px}.p2{left:96px;top:933px}.p3{left:690px;top:933px}.p4{left:96px;top:1724px}.p5{left:690px;top:1724px}
.strip{position:absolute;left:0;top:0;width:34px;height:100%;background:var(--board-edge)}
.band{position:absolute;left:37px;top:0;width:44px;height:513px;background:var(--band)}
.band-title{position:absolute;left:59px;top:256px;transform:translate(-50%,-50%) rotate(-90deg);white-space:nowrap;font-family:"Fira Sans",sans-serif;font-weight:800;font-size:36px;color:#111}
.guide{position:absolute;left:57px;top:600px;width:1px;height:105px;border-left:1px dashed #777}
.brand{position:absolute;left:14px;top:540px;width:90px;display:flex;flex-direction:column;align-items:center;gap:6px;font-family:"Montserrat",sans-serif;font-weight:600;font-size:11px;line-height:13px;color:var(--white);text-align:center}
.brand-dot{width:14px;height:14px;border-radius:50%;background:var(--white)}
.pin{position:absolute;right:55px;top:14px;width:9px;height:9px;border-radius:50%;background:var(--pin);box-shadow:0 0 0 2px rgba(210,32,42,.3)}
.abs{position:absolute}
.title{font-family:"Yanone Kaffeesatz",sans-serif;font-weight:600;color:var(--accent);line-height:1}
.heading{position:absolute;left:95px;width:375px;display:flex;align-items:center;gap:10px;font-family:"Yanone Kaffeesatz",sans-serif;font-weight:600;font-size:26px;color:var(--accent);white-space:nowrap}
.heading::before,.heading::after{content:"";flex:1;height:4px;background:var(--rule);opacity:.7}
.heading.left::before{display:none}
.heading.left::after{display:none}
.small{font-size:7.2px;line-height:10.5px}
.tiny{font-size:6.4px;line-height:8.6px;color:var(--text-dim)}
.r{text-align:right}.c{text-align:center}
.price{color:var(--accent);margin-left:3px}
.g{color:var(--accent)}
.w{color:var(--white)}
.step-num{position:absolute;width:22px;height:22px;margin:-11px 0 0 -11px;border-radius:50%;background:var(--accent);border:2px solid var(--board);box-shadow:0 0 0 1px var(--accent);color:var(--white);font-family:"Yanone Kaffeesatz",sans-serif;font-weight:600;font-size:16px;line-height:18px;text-align:center}
.step-lead{font-family:"Yanone Kaffeesatz",sans-serif;font-size:13px;line-height:12px;color:var(--accent)}
.step-lead b{color:var(--white);font-weight:600}
.art{position:absolute;background:linear-gradient(90deg,rgba(255,255,255,.12),rgba(255,255,255,.05));border-radius:3px}
.photo{position:absolute;background:linear-gradient(135deg,#3f78b0,#6a9fcf 45%,#d9c9a3 60%,#8a5a2c)}
.photo.dark{background:linear-gradient(135deg,#3a3a3a,#6b6b6b 45%,#c8b28a 60%,#7b4b23)}
.photo.can{background:linear-gradient(135deg,#3b7ab8,#5f9bd0 40%,#c23a2e 55%,#3b7ab8)}
.item-name{font-family:"Yanone Kaffeesatz",sans-serif;font-weight:600;font-size:11px;line-height:11px;color:var(--accent);text-transform:uppercase}
.item-desc{font-size:6.6px;line-height:8.4px;color:var(--text-dim);margin-top:2px}
.label{font-family:"Yanone Kaffeesatz",sans-serif;font-size:10px;color:var(--accent);text-transform:uppercase}
.vrule{position:absolute;width:0;border-left:1px dotted #777}
.hrule{position:absolute;height:0;border-top:1px dotted #777}
.box{position:absolute;border:1px dotted var(--rule)}
.box-title{position:absolute;font-family:"Yanone Kaffeesatz",sans-serif;font-weight:600;font-size:17px;color:var(--white);background:var(--board);padding:0 6px;transform:translateX(-50%);white-space:nowrap}
.offer{position:absolute;width:64px;height:64px;border-radius:50%;background:var(--accent);color:var(--white);font-family:"Yanone Kaffeesatz",sans-serif;font-weight:600;font-size:11px;line-height:11px;display:flex;align-items:center;justify-content:center;text-align:center}
</style>
</head>
<body>
<div class="stage">

<!-- Page: Souvlaki pita wrap and platters -->
<section class="page p1">
  <div class="strip"></div><div class="band"></div>
  <div class="band-title">Souvlaki Bar and Grill</div>
  <div class="brand"><span class="brand-dot"></span>Fennel &amp; Fig</div>
  <div class="guide"></div>
  <div class="pin"></div>

  <div class="abs title c" style="left:95px;width:375px;top:22px;font-size:26px">Our Souvlaki Pita Wrap <span style="margin-left:6px">5.50</span></div>
  <div class="abs c small" style="left:120px;width:325px;top:50px;font-size:7.6px">Get a whole meal containing protein, sauce and salad<br>with our delicious <span class="g">Greek Pita Wraps!</span></div>

  <svg class="abs" style="left:0;top:0" width="501" height="709" viewBox="0 0 501 709">
    <path d="M283 80 C283 100 252 105 252 120 M252 144 C252 165 313 168 313 184 M313 207 C313 226 250 232 250 248 M250 271 C250 290 313 295 313 311 M313 334 C313 350 250 345 250 350" fill="none" stroke="var(--accent)" stroke-width="1" stroke-dasharray="2 3"/>
  </svg>

  <div class="abs r small" style="left:90px;width:145px;top:89px;line-height:11px">
    Chicken<span class="price">0.50</span><br>Pork<span class="price">0.50</span><br>Gyros Chicken<span class="price">1.50</span><br>Gyros Pork<span class="price">1.50</span><br>Mixed Gyros (chicken and pork)<span class="price">2.00</span><br>Kebab (lamb+beef)<span class="price">0.50</span><br>Sausage<span class="price">0.50</span><br>Haloumi (V)<span class="price">0.50</span>
  </div>
  <div class="step-num" style="left:252px;top:132px">1</div>
  <div class="abs step-lead" style="left:273px;top:118px;font-size:15px;line-height:14px">Choose<br>a <b>base.</b></div>
  <div class="art" role="img" aria-label="Line drawings of a chicken, a pig and a cow" style="left:330px;top:110px;width:135px;height:40px"></div>

  <div class="art" role="img" aria-label="Line drawings of two sauce bowls with spoons" style="left:130px;top:190px;width:80px;height:24px"></div>
  <div class="abs r step-lead" style="left:200px;width:98px;top:180px">Add one of our<br>delicious home<br>made sauces.</div>
  <div class="step-num" style="left:313px;top:195px">2</div>
  <div class="abs small w" style="left:333px;top:180px;line-height:12.5px">Tzatziki (V)<br>Tyrokafteri (V)<br>Burger Sauce</div>

  <div class="abs r" style="left:130px;width:100px;top:232px;font-family:'Lora',serif;font-style:italic;font-size:6.6px;line-height:8px;color:var(--text-dim)">You can add multiple<br>ingredients.</div>
  <div class="abs r small w" style="left:150px;width:80px;top:253px;line-height:12.5px">Fries<br>Tomatoes<br>Onions</div>
  <div class="step-num" style="left:250px;top:259px">3</div>
  <div class="abs step-lead" style="left:270px;top:240px">Finalise it with<br><b>the ingredients</b><br>of your choice.</div>
  <div class="art" role="img" aria-label="Line drawings of an onion, a tomato slice and fries" style="left:352px;top:238px;width:112px;height:36px"></div>

  <div class="art" role="img" aria-label="Line drawings of a cow and a pig" style="left:95px;top:308px;width:110px;height:32px"></div>
  <div class="abs r step-lead" style="left:200px;width:98px;top:312px">Feeling Hungry?<br>Add <b>extras.</b></div>
  <div class="step-num" style="left:313px;top:322px">4</div>
  <div class="abs small w" style="left:332px;top:290px;line-height:12.5px">Double Pita Bread<span class="price">1.00</span><br>Add Pork Skewer<span class="price">2.50</span><br>Add Chicken Skewer<span class="price">2.50</span><br>Add Kebab (lamb+beef)<span class="price">2.50</span><br>Add Sausage<span class="price">2.50</span><br>Add Haloumi<span class="price">1.90</span></div>

  <div class="abs title w" style="left:162px;top:356px;font-size:11px">TRY OUR</div>
  <div class="photo dark" role="img" aria-label="Two wrapped souvlaki pita wraps" style="left:112px;top:365px;width:85px;height:48px;border-radius:6px"></div>
  <div class="offer" style="left:219px;top:346px">Double<br>Souvlaki<br>Pita Wrap!</div>
  <div class="abs" style="left:292px;top:384px;font-family:'Yanone Kaffeesatz',sans-serif;font-size:13px;line-height:13px;color:var(--accent)">Buy two wraps for 10.5<br><span class="w" style="font-size:11px">Takeout only!</span></div>

  <div class="hrule" style="left:95px;width:375px;top:420px;border-color:var(--accent)"></div>

  <div class="abs title c" style="left:95px;width:375px;top:424px;font-size:24px">Our Open Souvlaki Platters</div>
  <div class="vrule" style="left:287px;top:455px;height:150px"></div>

  <div class="abs title w" style="left:108px;top:458px;font-size:17px">Skewers Platter <span class="g" style="margin-left:6px">10.00</span></div>
  <div class="abs c tiny" style="left:112px;width:160px;top:479px">Homemade souvlaki is taken from the best part of the meat to create the perfect succulent grilled experience.</div>
  <div class="abs label" style="left:196px;top:513px">Meat Options</div>
  <div class="abs r small w" style="left:100px;width:165px;top:527px;line-height:12px">2 x Chicken Skewers<br>3 x Chicken Skewers<span class="price">3.00</span><br>2 x Pork Skewers<br>3 x Pork Skewers<span class="price">3.00</span><br>2 x Kebab (lamb+beef)<br>3 x Kebab (lamb+beef)<span class="price">3.00</span></div>

  <div class="abs title w" style="left:298px;top:458px;font-size:17px">Gyros Platter<sup style="font-size:8px">*</sup> <span class="g" style="margin-left:6px">13.00</span></div>
  <div class="abs tiny" style="left:298px;width:170px;top:479px">Generous portion served with refreshing tzatziki sauce, pita bread, fries, onion, tomatoes and lettuce.</div>
  <div class="abs label" style="left:298px;top:513px">Meat Options</div>
  <div class="abs small w" style="left:298px;top:527px;line-height:12px">Meat Options | Chicken Gyros 200gr<br>Pork Gyros 200gr<br>Mixed Gyros (chicken and pork) 200gr<span class="price">1.00</span><br>Chicken Gyros 300gr<span class="price">3.50</span><br>Pork Gyros 300gr<span class="price">3.50</span><br>Mixed Gyros (chicken and pork) 300gr<span class="price">4.50</span></div>

  <div class="box" style="left:143px;top:616px;width:277px;height:64px"></div>
  <div class="box-title" style="left:282px;top:605px">Choose Your...</div>
  <div class="abs" style="left:155px;top:632px"><div class="label">Sides<span style="font-size:8px">*</span></div><div class="small w">Fries<br>Side Salad<span class="price">2.50</span></div></div>
  <div class="abs" style="left:245px;top:630px"><div class="label">Extras</div><div class="small w" style="margin-top:5px">Extra Haloumi<span class="price">3.50</span><br>Extra Tzatziki<span class="price">3.00</span></div></div>
  <div class="abs" style="left:350px;top:632px"><div class="label">Pita Bread</div><div class="small w">1 x Pita<br>2 x Pita<span class="price">1.00</span></div></div>
  <div class="abs c tiny" style="left:95px;width:375px;top:687px">★ Platters with no sides/extras/pita bread only</div>
</section>

<!-- Page: From our grill -->
<section class="page p2">
  <div class="strip"></div><div class="band"></div>
  <div class="band-title">Souvlaki Bar and Grill</div>
  <div class="brand"><span class="brand-dot"></span>Fennel &amp; Fig</div>
  <div class="guide"></div>
  <div class="pin"></div>
  <div class="heading" style="top:35px">From Our Grill</div>

  <div class="vrule" style="left:286px;top:82px;height:300px"></div>
  <div class="hrule" style="left:95px;width:375px;top:225px"></div>
  <div class="hrule" style="left:95px;width:150px;top:382px"></div>

  <div class="photo" role="img" aria-label="Grilled fillets with fries on a plate" style="left:97px;top:85px;width:98px;height:78px"></div>
  <div class="abs" style="left:198px;top:86px"><div class="label" style="font-size:8px">Meat Options</div><div class="small">Chicken (Halal)<br>Fillet<br>Pork Fillet</div></div>
  <div class="abs" style="left:97px;top:170px;width:180px"><div class="item-name">Fillets <span style="margin-left:3px">13.00</span></div><div class="item-desc">Grilled tender pork or chicken fillets topped with an oregano and lemon sauce. Served with fries.</div></div>

  <div class="photo" role="img" aria-label="Village sausages with fries" style="left:302px;top:85px;width:98px;height:78px"></div>
  <div class="abs" style="left:404px;top:86px"><div class="label" style="font-size:8px">Dressing</div><div class="small">Mustard<br>Lemon</div></div>
  <div class="abs" style="left:302px;top:170px;width:170px"><div class="item-name">Village Sausages <span style="margin-left:3px">9.50</span></div><div class="item-desc">Two large grilled sausages from Thrace served with mustard or lemon dressing. Served with fries.</div></div>

  <div class="photo dark" role="img" aria-label="Sirloin steak with salad" style="left:97px;top:238px;width:98px;height:78px"></div>
  <div class="abs" style="left:202px;top:238px"><div class="label" style="font-size:8px;line-height:10px">Preferred<br>Cooking</div><div class="small" style="line-height:10px">Rare/ Medium<br>Rare<br>Medium/<br>Medium Well/<br>Well done</div></div>
  <div class="abs" style="left:97px;top:324px;width:180px"><div class="item-name">Sirloin Steak<sup style="font-size:7px">*</sup> <span style="margin-left:3px">24.50</span></div><div class="item-desc">Highly desired cut of meat has a beefier flavour, less fat and medium tender, as it comes from an area where muscles get more exercise.</div></div>

  <div class="photo dark" role="img" aria-label="Ribeye steak with salad" style="left:302px;top:238px;width:98px;height:78px"></div>
  <div class="abs" style="left:407px;top:238px"><div class="label" style="font-size:8px;line-height:10px">Preferred<br>Cooking</div><div class="small" style="line-height:10px">Rare/ Medium<br>Rare<br>Medium/<br>Medium Well/<br>Well done</div></div>
  <div class="abs" style="left:302px;top:324px;width:170px"><div class="item-name">Ribeye Steak <span style="margin-left:3px">24.50</span></div><div class="item-desc">Highly desired cut of meat has full flavour, soft and rich texture and juicy finish.</div></div>

  <div class="photo" role="img" aria-label="Lamb cutlets with fries" style="left:97px;top:393px;width:98px;height:78px"></div>
  <div class="abs" style="left:97px;top:478px;width:130px"><div class="item-name">Lamb Cutlets <span style="margin-left:3px">16.00</span></div><div class="item-desc">Tender lamb cutlets grilled to perfection and served with fries.</div></div>

  <div class="box" style="left:243px;top:393px;width:228px;height:120px;border-right:none;border-bottom:none"></div>
  <div class="box-title" style="left:365px;top:382px">Choose Your...</div>
  <div class="abs" style="left:275px;top:420px"><div class="label">Sides</div><div class="small w">Fries<br>Side Salad<span class="price">2.50</span></div></div>
  <div class="abs" style="left:377px;top:417px"><div class="label">Extras<span style="font-size:8px">*</span></div><div class="small w">Extra Haloumi<span class="price">3.50</span><br>Extra Tzatziki<span class="price">3.00</span></div></div>
  <div class="abs" style="left:275px;top:470px"><div class="label">Pita Bread</div><div class="small w">1 x Pita<br>2 x Pita<span class="price">1.00</span></div></div>
  <div class="abs" style="left:377px;top:482px;width:95px;font-family:'Lora',serif;font-style:italic;font-size:6.2px;line-height:8px;color:var(--text-dim)">★ From our grill with no sides/ extras/pita bread only</div>

  <div class="photo dark" role="img" aria-label="Three souvlaki pita wraps in paper wrappers" style="left:110px;top:548px;width:370px;height:150px;border-radius:40px 40px 10px 10px"></div>
</section>

<!-- Page: Meal deals -->
<section class="page p3">
  <div class="strip"></div><div class="band"></div>
  <div class="band-title">Souvlaki Bar and Grill</div>
  <div class="brand"><span class="brand-dot"></span>Fennel &amp; Fig</div>
  <div class="guide"></div>
  <div class="pin"></div>
  <div class="heading left" style="top:35px;font-size:25px">Meal Deals . Starter Combo . Set Menu</div>

  <div class="vrule" style="left:215px;top:80px;height:415px"></div>
  <div class="vrule" style="left:353px;top:80px;height:415px"></div>
  <div class="hrule" style="left:95px;width:375px;top:288px"></div>

  <div class="photo" role="img" aria-label="Meal for one: wrap, salad and drink" style="left:95px;top:85px;width:98px;height:78px"></div>
  <div class="abs" style="left:95px;top:170px;width:112px"><div class="item-name">Meal Deal for One<br>13.50</div><div class="item-desc">Get a full Greek meal for one person. Our delicious Pita Souvlaki Wrap that can be customised to your preference. Served with side salad, greek donuts and soft drink.</div></div>

  <div class="photo" role="img" aria-label="Meal for two: wraps, salads and dessert" style="left:232px;top:85px;width:98px;height:78px"></div>
  <div class="abs" style="left:232px;top:170px;width:112px"><div class="item-name">Meal Deal for 2<br>24.00</div><div class="item-desc">Get a full Greek meal for two. 2 x delicious Pita Souvlaki Wrap that can be individually customised to your taste. Pick any of our healthy Salad options. Choose a drink each. And finish it sharing one of our exquisite desserts.</div></div>

  <div class="photo" role="img" aria-label="Family meal: four wraps with salads" style="left:370px;top:85px;width:98px;height:78px"></div>
  <div class="abs" style="left:370px;top:170px;width:100px"><div class="item-name">Family Meal Deal<br>for 4 <span style="margin-left:3px">45.00</span></div><div class="item-desc">Get a full Greek meal for four. 4 x delicious Pita Souvlaki Wrap that can be individually customised to your taste. Pick any of our healthy Salad options. Choose 2 drinks. And finish it sharing two of our exquisite desserts.</div></div>

  <div class="photo" role="img" aria-label="Starter combo of dips and pita" style="left:95px;top:297px;width:98px;height:78px"></div>
  <div class="abs" style="left:95px;top:382px;width:112px"><div class="item-name">Starter Combo<br>11.50</div><div class="item-desc">Can't make up your mind on our starters? Indulge in our Greek Starter Combo. You can choose 4 of a great selection of cold and warm starters.</div></div>

  <div class="photo" role="img" aria-label="Family meal with wraps and salads" style="left:232px;top:297px;width:98px;height:78px"></div>
  <div class="abs" style="left:232px;top:382px;width:112px"><div class="item-name">Family Meal Deal<br>for 4 <span style="margin-left:3px">45.00</span></div><div class="item-desc">Get a full Greek meal for four. 4 x delicious Pita Souvlaki Wrap that can be individually customised to your taste. Pick any of our healthy Salad options and 2 x Starters. Choose 2 drinks. And finish it sharing two of our exquisite desserts.</div></div>

  <div class="photo" role="img" aria-label="Set menu spread of grilled meats and dips" style="left:370px;top:297px;width:98px;height:78px"></div>
  <div class="abs" style="left:370px;top:382px;width:100px"><div class="item-name">Set Menu for 2+<br>People <span style="margin-left:3px">60.00</span></div><div class="item-desc">Marinated Kalamata Giant Olives, Tyrokafteri, Tzatziki, 2 x Chicken Skewers, 2 x Pork Skewers, 2 x Lamb Cutlet Pieces, 2 x Haloumi, 1 x Village Sausage, Chicken Fillets, Pork Fillets, Fries. Your choice of Salad. Your choice of Dessert.</div></div>

  <div class="box" style="left:100px;top:535px;width:245px;height:170px;border-bottom:none"></div>
  <div class="box-title" style="left:280px;top:514px">Choose Your...</div>
  <div class="abs" style="left:113px;top:541px"><div class="label">Base</div><div class="tiny" style="line-height:9px">Chicken<span class="price">0.50</span><br>Pork<span class="price">0.50</span><br>Gyros Chicken<span class="price">1.50</span><br>Gyros Pork<span class="price">1.50</span><br>Mixed Gyros (chicken and<br>pork)<span class="price">2.00</span><br>Kebab (lamb+beef)<span class="price">0.50</span><br>Sausage<span class="price">0.50</span><br>Haloumi (V)<span class="price">0.50</span></div></div>
  <div class="abs" style="left:113px;top:645px"><div class="label">Sauce</div><div class="tiny" style="line-height:9px">Tzatziki (V)<br>Tyrokafteri (V)<br>Burger Sauce</div></div>
  <div class="abs" style="left:231px;top:555px"><div class="label">Extras</div><div class="tiny" style="line-height:9px">Double Pita Bread<span class="price">1.00</span><br>Add Pork Skewer<span class="price">2.50</span><br>Add Chicken Skewer<span class="price">2.50</span><br>Add Kebab (lamb+beef)<span class="price">2.50</span><br>Add Sausage<span class="price">2.50</span><br>Add Haloumi<span class="price">1.90</span></div></div>
  <div class="abs" style="left:231px;top:645px"><div class="label">Ingredients</div><div class="tiny" style="line-height:9px">Fries<br>Tomatoes<br>Onions</div></div>

  <div class="box" style="left:350px;top:525px;width:120px;height:180px;border-bottom:none"></div>
  <div class="abs" style="left:368px;top:532px"><div class="label" style="line-height:11px">Choose 4. For<br>Starter Combo<br>Only</div><div class="tiny" style="line-height:9px;margin-top:2px">Tzatziki<br>White Taramosalata<br>Tirokafteri<br>Giant Olives<br>Side Salad<br>Gigantes<br>Fava<br>Hummus</div></div>
  <div class="abs" style="left:368px;top:655px"><div class="label">Pita Bread</div><div class="tiny" style="line-height:9px">1 x Pita<br>2 x Pita<span class="price">1.00</span></div></div>
</section>

<!-- Page: Salads and drinks -->
<section class="page p4">
  <div class="strip"></div><div class="band"></div>
  <div class="band-title">Souvlaki Bar and Grill</div>
  <div class="brand"><span class="brand-dot"></span>Fennel &amp; Fig</div>
  <div class="guide"></div>
  <div class="pin"></div>
  <div class="heading" style="top:33px">Salads</div>

  <div class="vrule" style="left:217px;top:78px;height:310px"></div>
  <div class="vrule" style="left:354px;top:78px;height:310px"></div>
  <div class="hrule" style="left:95px;width:375px;top:228px"></div>

  <div class="photo" role="img" aria-label="Greek salad with feta and olives" style="left:97px;top:80px;width:103px;height:78px"></div>
  <div class="abs" style="left:97px;top:165px;width:112px"><div class="item-name">Greek Salad (V) <span style="margin-left:2px">8.50</span></div><div class="item-desc">Greek feta, tomato, cucumber, green pepper, onion, olives &amp; olive oil. (Vegetarian)</div></div>
  <div class="photo" role="img" aria-label="Caesar salad with chicken" style="left:233px;top:80px;width:105px;height:78px"></div>
  <div class="abs" style="left:233px;top:165px;width:112px"><div class="item-name">Our Caesar Salad <span style="margin-left:2px">10.00</span></div><div class="item-desc">Green salad mixed with grilled Chicken Fillet, Cherry Tomatoes, Caesar Sauce &amp; Grated Parmesan.</div></div>
  <div class="photo" role="img" aria-label="Side salad of lettuce and tomato" style="left:371px;top:80px;width:104px;height:78px"></div>
  <div class="abs" style="left:371px;top:165px;width:104px"><div class="item-name">Side Salad <span style="margin-left:2px">3.00</span></div><div class="item-desc">Lettuce, tomato, cucumber, onion and grated feta.</div></div>

  <div class="photo" role="img" aria-label="House salad with baby kale and lamb's lettuce" style="left:97px;top:237px;width:103px;height:78px"></div>
  <div class="abs" style="left:97px;top:323px;width:112px"><div class="item-name">House Special Salad<br>9.50</div><div class="item-desc">Baby kale, tender baby leaves and a mix of strong and crunchy radicchio, lamb's lettuce and crisp frisee, pomegranate and dry figs. Sauteed with balsamic and honey sauce.</div></div>
  <div class="photo" role="img" aria-label="Cretan dakos salad" style="left:233px;top:237px;width:105px;height:78px"></div>
  <div class="abs" style="left:233px;top:323px;width:112px"><div class="item-name">Cretan Dakos Salad (V)<br>8.50</div><div class="item-desc">Cretan rusk soaked in Greek extra virgin olive oil, topped with chopped tomato, feta cheese, olives, spring onion &amp; oregano. (Vegetarian)</div></div>
  <div class="photo" role="img" aria-label="Haloumi salad with tomatoes" style="left:371px;top:237px;width:104px;height:78px"></div>
  <div class="abs" style="left:371px;top:323px;width:104px"><div class="item-name">Haloumi Salad <span style="margin-left:2px">9.50</span></div><div class="item-desc">Haloumi salad with cocktail tomatoes, red and yellow peppers, mix lettuce, cucumber, spring onions and a yogurt &amp; mint dressing.</div></div>

  <div class="heading" style="top:395px">Drinks</div>
  <div class="photo can" role="img" aria-label="Bottle of orange juice" style="left:97px;top:440px;width:85px;height:76px"></div>
  <div class="abs" style="left:97px;top:521px;width:92px"><div class="item-name">Lemoni Orange <span style="margin-left:2px">2.00</span></div><div class="item-desc">Natural juice from 100% Greek oranges, and a balanced quantity of carbonates.</div></div>
  <div class="photo can" role="img" aria-label="Can of diet cola" style="left:194px;top:440px;width:86px;height:76px"></div>
  <div class="abs" style="left:194px;top:521px;width:92px"><div class="item-name">Koura Cola Diet<br>2.00</div><div class="item-desc">A sugar-free and no-calorie soft drink.</div></div>
  <div class="photo can" role="img" aria-label="Can of zero sugar cola" style="left:292px;top:440px;width:85px;height:76px"></div>
  <div class="abs" style="left:292px;top:521px;width:92px"><div class="item-name">Koura Cola Zero <span style="margin-left:2px">2.00</span></div><div class="item-desc">New and improved sugar free cola, tastes even more like the classic original taste.</div></div>
  <div class="photo can" role="img" aria-label="Can of lemon lime soda" style="left:388px;top:440px;width:87px;height:76px"></div>
  <div class="abs" style="left:388px;top:521px;width:88px"><div class="item-name">Zesty Lime <span style="margin-left:2px">2.00</span></div><div class="item-desc">Crisp, refreshing and clean-tasting lemon and lime flavored soft drink.</div></div>

  <div class="photo can" role="img" aria-label="Bottle of lemonade" style="left:97px;top:568px;width:85px;height:76px"></div>
  <div class="abs" style="left:97px;top:649px;width:92px"><div class="item-name">Lemoni Lemonade <span style="margin-left:2px">2.00</span></div><div class="item-desc">Unique sweet &amp; sour flavor and intense aroma, in combination.</div></div>
  <div class="photo can" role="img" aria-label="Can of cola" style="left:194px;top:568px;width:86px;height:76px"></div>
  <div class="abs" style="left:194px;top:649px;width:92px"><div class="item-name">Koura Cola <span style="margin-left:2px">2.00</span></div><div class="item-desc">A sweetened carbonated beverage.</div></div>
  <div class="photo can" role="img" aria-label="Can of sparkling apple juice" style="left:292px;top:568px;width:85px;height:76px"></div>
  <div class="abs" style="left:292px;top:649px;width:92px"><div class="item-name">Applefizz <span style="margin-left:2px">2.00</span></div><div class="item-desc">Gently Sparkling Apple Juice</div></div>
  <div class="photo can" role="img" aria-label="Bottle of still water" style="left:388px;top:568px;width:87px;height:76px"></div>
  <div class="abs" style="left:388px;top:649px;width:88px"><div class="item-name">Pindos Spring 500ml<br>Natural Mineral<br>Still Water <span style="margin-left:2px">1.50</span></div></div>
</section>

<!-- Page: Starters -->
<section class="page p5">
  <div class="strip"></div><div class="band"></div>
  <div class="band-title">Souvlaki Bar and Grill</div>
  <div class="brand"><span class="brand-dot"></span>Fennel &amp; Fig</div>
  <div class="guide"></div>
  <div class="pin"></div>
  <div class="heading" style="top:33px">Cold Starters</div>

  <div class="vrule" style="left:220px;top:76px;height:284px"></div>
  <div class="vrule" style="left:357px;top:76px;height:284px"></div>
  <div class="hrule" style="left:95px;width:375px;top:212px"></div>

  <div class="photo" role="img" aria-label="Tyrokafteri dip" style="left:105px;top:78px;width:95px;height:77px"></div>
  <div class="abs" style="left:105px;top:160px;width:110px"><div class="item-name">Tyrokafteri (GF) <span style="margin-left:2px">5.00</span></div><div class="item-desc">Handmade dip from Greek feta cheese, mild pepper &amp; spices, served with pitta bread. (Gluten Free)</div></div>
  <div class="photo dark" role="img" aria-label="Tzatziki dip" style="left:235px;top:78px;width:95px;height:77px"></div>
  <div class="abs" style="left:235px;top:160px;width:112px"><div class="item-name">Tzatziki (GF) <span style="margin-left:2px">4.00</span></div><div class="item-desc">Authentic Greek yoghurt, blended with mint, garlic, dill &amp; other herbs. The Greek's favourite dip, served with pitta bread. (Gluten Free)</div></div>
  <div class="photo" role="img" aria-label="Hummus dip" style="left:372px;top:78px;width:95px;height:77px"></div>
  <div class="abs" style="left:372px;top:160px;width:100px"><div class="item-name">Hummus <span style="margin-left:2px">4.00</span></div><div class="item-desc">Pureed chickpeas, tahini, lemon, garlic drizzled with extra virgin olive oil served with pita bread</div></div>

  <div class="photo" role="img" aria-label="Marinated Kalamata olives" style="left:105px;top:222px;width:95px;height:78px"></div>
  <div class="abs" style="left:105px;top:308px;width:112px"><div class="item-name">Marinated Kalamata<br>Giant Olives (GF) <span style="margin-left:2px">3.80</span></div><div class="item-desc" style="font-size:5.8px;line-height:7px">Baby kale, tender baby leaves. The Kalamata olive is a large, black olive with a smooth, meaty texture named after the city of Kalamata in the southern Peloponnese, Greece.</div></div>
  <div class="photo" role="img" aria-label="White taramosalata dip" style="left:235px;top:222px;width:95px;height:78px"></div>
  <div class="abs" style="left:235px;top:308px;width:112px"><div class="item-name">White Taramosalata<br>4.00</div><div class="item-desc">Rich, creamy, made fresh with cod roe, lemon juice, and extra virgin olive oil. Served with pitta bread.</div></div>
  <div class="photo" role="img" aria-label="Feta cheese with olive oil and oregano" style="left:372px;top:222px;width:95px;height:78px"></div>
  <div class="abs" style="left:372px;top:308px;width:100px"><div class="item-name">Feta Cheese with Olive<br>Oil &amp; Oregano (GF)<br>5.00</div><div class="item-desc">Greek feta in extra virgin olive oil, dusted with oregano. (Gluten Free)</div></div>

  <div class="heading" style="top:366px">Hot Starters</div>
  <div class="vrule" style="left:220px;top:412px;height:160px"></div>
  <div class="vrule" style="left:357px;top:412px;height:160px"></div>
  <div class="hrule" style="left:95px;width:375px;top:580px"></div>

  <div class="photo" role="img" aria-label="Gigantes beans in tomato sauce" style="left:105px;top:420px;width:95px;height:78px"></div>
  <div class="abs" style="left:105px;top:505px;width:112px"><div class="item-name">Gigantes Starter (V)<br>4.00</div><div class="item-desc">A classic Greek recipe, consisting of giant beans baked in a tomato sauce along with plenty of fresh herbs. (Vegan)</div></div>
  <div class="photo" role="img" aria-label="Fava yellow split pea puree" style="left:235px;top:420px;width:95px;height:78px"></div>
  <div class="abs" style="left:235px;top:505px;width:112px"><div class="item-name">Fava Starter (V) <span style="margin-left:2px">4.00</span></div><div class="item-desc">Authentic Santorini island yellow split pea puree. Served with capers and a variety of mixed onions. (Vegan)</div></div>
  <div class="photo" role="img" aria-label="Grilled haloumi slices" style="left:372px;top:420px;width:95px;height:78px"></div>
  <div class="abs" style="left:372px;top:505px;width:100px"><div class="item-name">Grilled Haloumi (V)<br>5.00</div><div class="item-desc">The favourite Cypriot cheese served with lemon slices &amp; fresh mint.</div></div>

  <div class="photo" role="img" aria-label="Baked feta in filo pastry with honey" style="left:105px;top:595px;width:95px;height:75px"></div>
  <div class="abs" style="left:205px;top:596px;width:75px"><div class="item-name">Baked Feta<br>Cheese with<br>Honey and<br>Sesame <span style="margin-left:2px">6.00</span></div><div class="item-desc">Feta cheese wrapped in filo pastry with honey and sesame.</div></div>
  <div class="photo" role="img" aria-label="Bowl of fries" style="left:290px;top:595px;width:95px;height:75px"></div>
  <div class="abs" style="left:390px;top:596px;width:80px"><div class="item-name">Fries (V) <span style="margin-left:2px">4.00</span></div><div class="item-desc">Crunchy fries dusted with coarse salt &amp; oregano.</div></div>
</section>

</div>
</body>
</html>
```